1 Page for Computer Repair Website

Looking for a 1 page website with a design that compliments the business card and pamphlet that have already been made (attached files). It should look business professional and easy to read. Email and phone number should be somewhere near the top of the website, visible when the page loads. I don't want any forms for people to mess with. No "Contact Us" form or entering in email for newsletter. Customers will just be looking at this site to confirm we are professionals and have our business in order.

Target Market(s)

Home and small business

Industry/Entity Type

Computer Repair

Coding

Coded - Design and coding required

Number of Pages Required

1 page

Font styles to use
Other font styles liked:
• Helvetica variations used in pamphlet and card

Colors
0455a3
cfdeed
85abd2
3276b5
85cae6
ffffff

Requirements
Must have
• Compliment the pamphlet and business card in color choices and font use. Pleasing to the eye and easy to read through categories and text.
Should not have
• Forms. No "enter name and email here" or anything of the sort.

```html
<!DOCTYPE html>
<html lang="en">
<head>
<meta charset="utf-8">
<title>NorthByte – Computer Service &amp; Repair</title>
<link rel="stylesheet" href="https://fonts.googleapis.com/css2?family=Arimo:wght@400;700&display=swap">
<style>
:root{
  --blue-deep:#0455a3;
  --blue-mid:#3276b5;
  --blue-soft:#85abd2;
  --blue-sky:#85cae6;
  --blue-mist:#cfdeed;
  --white:#ffffff;
  --ink:#2b3440;
  --text-grey:#7a8591;
  --band-grey:#ededed;
}
*{box-sizing:border-box;margin:0;padding:0}
html,body{width:736px;height:1200px;overflow:hidden;background:var(--white)}
body{position:relative;font-family:"Arimo",Helvetica,Arial,sans-serif;color:var(--ink)}
.abs{position:absolute}

/* Hero */
.hero-photo{left:0;top:0;width:736px;height:300px;
  background:linear-gradient(160deg,#0d3f78 0%,#1f5f9e 30%,#9cc0df 55%,#d7e4f1 68%,#4f86bd 85%,#0b3a6e 100%)}
.brand{left:14px;top:12px;font-size:24px;font-weight:700;color:var(--white);letter-spacing:.5px}
.contact{right:22px;top:14px;text-align:right;color:var(--white);font-size:14px;line-height:19px}
.hero-title{left:61px;top:160px;color:var(--white);font-size:27px;font-weight:700;line-height:30px;text-transform:uppercase}
.hero-dots{left:61px;top:234px;display:flex;gap:6px}
.hero-dots span{width:6px;height:6px;border-radius:50%;background:var(--white)}

/* Service tiles */
.tiles{left:61px;top:275px;width:614px;height:155px;display:flex;box-shadow:0 8px 14px rgba(0,0,0,.18)}
.tile{flex:1;color:var(--white);text-align:center;padding:16px 22px 0}
.tile--deep{background:var(--blue-deep)}
.tile--mid{background:var(--blue-mid)}
.tile--soft{background:var(--blue-soft)}
.tile svg{width:30px;height:26px;display:block;margin:0 auto 8px}
.tile h3{font-size:15px;line-height:18px;font-weight:700;text-transform:uppercase;margin-bottom:10px}
.tile p{font-size:8.5px;line-height:12px}

/* Section headings */
.section-title{font-size:19px;font-weight:700;color:var(--blue-deep);text-transform:uppercase}
.rule{height:1px;background:var(--blue-mist)}
.body-text{font-size:9px;line-height:13px;color:var(--text-grey)}

/* About */
.about-title{left:61px;top:488px}
.about-rule{left:61px;top:516px;width:330px}
.about-text{left:61px;top:526px;width:330px}
.about-text p+p{margin-top:10px}
.about-photo{left:417px;top:465px;width:252px;height:152px;
  background:linear-gradient(180deg,#e9eef3 0%,#c4ccd5 55%,#5b6673 100%)}

/* Our services band */
.services-band{left:0;top:650px;width:736px;height:285px;background:var(--band-grey)}
.services-title{left:61px;top:680px}
.services-arrows{left:640px;top:684px;display:flex;gap:12px}
.services-arrows svg{width:9px;height:12px}
.service{top:718px;width:184px}
.service-photo{width:184px;height:104px}
.service h4{margin-top:22px;font-size:12.5px;font-weight:400;color:var(--blue-deep);text-transform:uppercase}
.service p{margin-top:8px}
.photo-malware{background:linear-gradient(135deg,#0b2b57,#2a66a8 60%,#0e1f3c)}
.photo-hardware{background:linear-gradient(135deg,#5a5e63,#a8acb0 50%,#3e4246)}
.photo-migration{background:linear-gradient(135deg,#0a2345,#1e4d86 55%,#081a33)}

/* Why choose us */
.why-photo{left:0;top:955px;width:305px;height:185px;
  background:linear-gradient(170deg,#ffffff 0%,#e6ebf0 40%,#9aa6b3 100%)}
.why-title{left:348px;top:998px}
.why-list{left:348px;top:1030px;list-style:none;width:330px}
.why-list li{display:flex;align-items:center;gap:8px;height:17px}
.why-list svg{width:9px;height:9px;flex:none}

/* Footer */
.footer{left:0;top:1172px;width:736px;height:28px;background:var(--blue-deep);display:flex;align-items:center;justify-content:space-between;padding:0 14px}
.footer small{font-size:8px;color:var(--white)}
.social{display:flex;gap:6px}
.social span{width:11px;height:11px;border-radius:50%;background:var(--blue-mist)}
</style>
</head>
<body>

<header>
  <div class="abs hero-photo" role="img" aria-label="Photo of hands typing on a laptop keyboard in blue light"></div>
  <div class="abs brand">NorthByte</div>
  <div class="abs contact">Call us: 555-014-2876<br>Email:hello@northbyte.example</div>
  <h1 class="abs hero-title">Computer<br>Service &amp; Repair</h1>
  <div class="abs hero-dots"><span></span><span></span><span></span></div>
</header>

<section class="abs tiles">
  <div class="tile tile--deep">
    <svg viewBox="0 0 30 26"><path d="M15 2 2 13h4v11h7v-7h4v7h7V13h4z" fill="#fff"/></svg>
    <h3>Residential<br>Services</h3>
    <p>Home computers repaired quickly, with fair pricing and friendly advice every time.</p>
  </div>
  <div class="tile tile--mid">
    <svg viewBox="0 0 30 26"><path d="M5 24V4h12v20zM19 24V10h6v14z" fill="#fff"/><path d="M8 7h2v2H8zm4 0h2v2h-2zM8 12h2v2H8zm4 0h2v2h-2zM8 17h2v2H8zm4 0h2v2h-2z" fill="#3276b5"/></svg>
    <h3>Business<br>Services</h3>
    <p>Office machines and networks kept running so your staff can keep working.</p>
  </div>
  <div class="tile tile--soft">
    <svg viewBox="0 0 30 26"><rect x="3" y="3" width="24" height="15" fill="none" stroke="#fff" stroke-width="2"/><path d="M11 23h8M15 18v5" stroke="#fff" stroke-width="2"/></svg>
    <h3>Remote<br>Support</h3>
    <p>Quick software fixes done securely online without leaving your desk or home.</p>
  </div>
</section>

<section>
  <h2 class="abs section-title about-title">About Us</h2>
  <div class="abs rule about-rule"></div>
  <div class="abs body-text about-text">
    <p>We are a local team of certified technicians helping homes and small businesses keep their computers fast, safe and reliable.</p>
    <p>From a single laptop to a full office network, we diagnose problems clearly, explain the options and fix it right the first time.</p>
  </div>
  <div class="abs about-photo" role="img" aria-label="Row of desktop computer monitors"></div>
</section>

<section>
  <div class="abs services-band"></div>
  <h2 class="abs section-title services-title">Our Services</h2>
  <div class="abs services-arrows">
    <svg viewBox="0 0 9 12"><path d="M7 1 2 6l5 5" fill="none" stroke="#2b3440" stroke-width="2"/></svg>
    <svg viewBox="0 0 9 12"><path d="M2 1l5 5-5 5" fill="none" stroke="#2b3440" stroke-width="2"/></svg>
  </div>
  <article class="abs service" style="left:61px">
    <div class="service-photo photo-malware" role="img" aria-label="Close-up of a circuit board in blue light"></div>
    <h4>Malware/Virus Removal</h4>
    <p class="body-text">Infections are removed and your system is scanned, cleaned and protected so it runs smoothly again.</p>
  </article>
  <article class="abs service" style="left:275px">
    <div class="service-photo photo-hardware" role="img" aria-label="Computer motherboard and components"></div>
    <h4>Hardware Repair</h4>
    <p class="body-text">Failing drives, screens, fans and boards are tested and replaced with quality parts at fair rates.</p>
  </article>
  <article class="abs service" style="left:486px">
    <div class="service-photo photo-migration" role="img" aria-label="Padlock over glowing digital circuitry"></div>
    <h4>Data Migration</h4>
    <p class="body-text">Files, photos and settings move safely to your new computer with nothing lost along the way.</p>
  </article>
</section>

<section>
  <div class="abs why-photo" role="img" aria-label="Hand reaching out of a laptop screen"></div>
  <h2 class="abs section-title why-title">Why Choose Us</h2>
  <ul class="abs why-list body-text">
    <li><svg viewBox="0 0 9 9"><path d="M1 5l2.5 2.5L8 2" fill="none" stroke="#3276b5" stroke-width="1.6"/></svg>Certified technicians with years of hands-on repair experience</li>
    <li><svg viewBox="0 0 9 9"><path d="M1 5l2.5 2.5L8 2" fill="none" stroke="#3276b5" stroke-width="1.6"/></svg>Clear upfront pricing with no hidden fees</li>
    <li><svg viewBox="0 0 9 9"><path d="M1 5l2.5 2.5L8 2" fill="none" stroke="#3276b5" stroke-width="1.6"/></svg>Fast turnaround for home and business clients</li>
    <li><svg viewBox="0 0 9 9"><path d="M1 5l2.5 2.5L8 2" fill="none" stroke="#3276b5" stroke-width="1.6"/></svg>Remote support available for quick software fixes</li>
    <li><svg viewBox="0 0 9 9"><path d="M1 5l2.5 2.5L8 2" fill="none" stroke="#3276b5" stroke-width="1.6"/></svg>Friendly service and honest, practical advice</li>
  </ul>
</section>

<footer class="abs footer">
  <small>© 2015 NorthByte. All rights reserved</small>
  <div class="social"><span></span><span></span><span></span><span></span><span></span></div>
</footer>

</body>
</html>
```